12" Touchscreen Interface Graphic Design

We have a touchscreen control system already designed with rudimentary graphics. The functionality is there, we need to make the graphics look more professional.
The new graphics design is to be 'modular' so that things can be moved within the touchscreen software.
By modular i mean that i need to for example add or remove pumps from the system, change the piping layout, move location of the various graphical elements.
I have enough graphics skills to be able to re-size, stretch, colorize the submitted design to adapt it specifically to the ongoing changing needs of the interface.
I can "cut up" the submitted design to make my individual graphical elements (for example 80x100px image for the pump) that i can then move around where i want for future systems that have different hardware configurations.
Attached are screenshots of how the interface looks at the moment, with some comments on the side.
The graphical elements need ideally to have the same pixel dimensions as on the screenshot. If changes are recommended for a specific reason, each element within the overall display should have dimensions in increments of 10px
Also attached is a screenshot from one of our other unrelated control systems that has a graphics style we would like to be close to.
Look and feel
Each slider illustrates characteristics of the customer's brand and the style your logo design should communicate.

```html
<!DOCTYPE html>
<html lang="en">
<head>
<meta charset="utf-8">
<title>Chiller Plant Control Panel</title>
<link rel="stylesheet" href="https://fonts.googleapis.com/css2?family=Open+Sans:wght@400;600;700&display=swap">
<style>
  :root {
    --bg: #000000;
    --panel: #0e0f1c;
    --panel-edge: #262a3e;
    --header: #171a2a;
    --field: #0a0b14;
    --field-edge: #3a3e55;
    --text: #ffffff;
    --muted: #c9cbd6;
    --pipe-yellow: #ffff00;
    --pipe-yellow-core: #ffff8a;
    --pipe-cyan: #16d6ea;
    --pipe-cyan-core: #8ff4ff;
    --run-green: #2e7d12;
    --pause-orange: #ff7b00;
    --stop-red: #b80c0c;
    --stop-red-dark: #7c0000;
    --start-grey: #9b9b9b;
    --reset-blue: #0c1296;
    --frame-dotted: #6d6d6d;
    --pump-light: #9a9a9a;
    --pump-dark: #4a4a4a;
  }
  * { box-sizing: border-box; margin: 0; padding: 0; }
  html, body { width: 1200px; height: 750px; overflow: hidden; background: var(--bg); }
  body { font-family: "Open Sans", Arial, sans-serif; color: var(--text); }

  .stage {
    position: relative; width: 1253px; height: 783px;
    transform: scale(0.9577); transform-origin: 0 0;
  }
  .abs { position: absolute; }

  .pipes { position: absolute; left: 0; top: 0; width: 1253px; height: 783px; z-index: 2; }
  .pipe-y { fill: none; stroke: var(--pipe-yellow); stroke-width: 7; filter: drop-shadow(0 0 2px #b5b500); }
  .pipe-y-core { fill: none; stroke: var(--pipe-yellow-core); stroke-width: 2; }
  .pipe-c { fill: none; stroke: var(--pipe-cyan); stroke-width: 7; }
  .pipe-c-core { fill: none; stroke: var(--pipe-cyan-core); stroke-width: 2; }
  .arrow-y { fill: var(--pipe-yellow); }
  .arrow-c { fill: var(--pipe-cyan); }

  .control-frame { left: 353px; top: 12px; width: 145px; height: 670px; border: 1px dotted var(--frame-dotted); z-index: 1; }

  .reading {
    position: absolute; z-index: 3; border-radius: 4px;
    display: flex; align-items: center; justify-content: center;
    font-weight: 700; font-size: 17px; color: #000;
  }
  .reading--yellow { background: var(--pipe-yellow); }
  .reading--cyan { background: var(--pipe-cyan); }

  /* Pumps */
  .pump-card {
    position: absolute; left: 133px; width: 129px; height: 142px; z-index: 1;
    background: var(--panel); border: 1px solid var(--panel-edge); border-radius: 4px;
  }
  .pump-card__title { position: absolute; top: 4px; width: 100%; text-align: center; font-size: 9.5px; font-weight: 600; }
  .pump-card__time {
    position: absolute; left: 6px; top: 22px; width: 118px; height: 18px;
    background: var(--field); border: 1px solid var(--field-edge); border-radius: 3px;
    font-size: 9.5px; font-weight: 600; text-align: center; line-height: 16px;
  }
  .pump-overlay { position: absolute; left: 133px; width: 129px; height: 142px; z-index: 4; }
  .pump-overlay__art {
    position: absolute; left: 40px; top: 46px; width: 48px; height: 62px; border-radius: 3px;
    background: linear-gradient(180deg, var(--pump-light), var(--pump-dark));
  }
  .pump-overlay__reset {
    position: absolute; left: 24px; top: 112px; width: 80px; height: 23px;
    background: var(--reset-blue); border-radius: 12px;
    font-size: 9px; font-weight: 600; text-align: center; line-height: 23px;
  }

  /* Target temperature */
  .target {
    left: 362px; top: 496px; width: 128px; height: 170px; z-index: 3;
    background: var(--panel); border: 1px solid #8a8a50; border-radius: 4px;
  }
  .target__title { position: absolute; top: 17px; width: 100%; text-align: center; font-size: 8.5px; font-weight: 600; }
  .target__value { position: absolute; top: 34px; width: 100%; text-align: center; font-size: 20px; font-weight: 700; }
  .target__btn {
    position: absolute; top: 77px; width: 55px; height: 53px;
    border: 1px solid #3a3e55; border-radius: 4px; background: #05060c;
    font-size: 20px; font-weight: 600; text-align: center; line-height: 50px;
  }

  /* Chillers */
  .chiller {
    position: absolute; width: 210px; height: 266px; z-index: 3;
    background: var(--panel); border: 1px solid var(--panel-edge); border-radius: 4px;
  }
  .chiller__name { position: absolute; top: -18px; width: 100%; text-align: center; font-size: 9.5px; font-weight: 600; }
  .chiller__temps { position: absolute; left: 0; top: 0; width: 100%; height: 33px; display: flex; background: var(--header); border-bottom: 1px solid var(--panel-edge); border-radius: 4px 4px 0 0; }
  .chiller__temp { flex: 1; text-align: center; line-height: 33px; font-size: 13px; font-weight: 700; }
  .chiller__temp + .chiller__temp { border-left: 1px solid var(--panel-edge); }
  .label { position: absolute; font-size: 8.5px; font-weight: 600; }
  .field {
    position: absolute; width: 63px; height: 16px;
    background: var(--field); border: 1px solid var(--field-edge); border-radius: 3px;
    font-size: 9.5px; font-weight: 600; text-align: right; padding-right: 4px; line-height: 14px;
  }
  .unit { position: absolute; font-size: 8px; color: var(--muted); font-weight: 600; }
  .pill {
    position: absolute; left: 84px; width: 119px; height: 19px; border-radius: 4px;
    font-size: 9.5px; font-weight: 600; text-align: center; line-height: 19px;
  }
  .pill--running { background: var(--run-green); }
  .pill--paused { background: var(--pause-orange); }
  .pill--time { background: var(--field); border: 1px solid var(--field-edge); line-height: 17px; }
  .chiller__action {
    position: absolute; left: -1px; bottom: -1px; width: 210px; height: 47px; border-radius: 0 0 5px 5px;
    font-size: 11px; text-align: center; line-height: 47px;
    background: linear-gradient(var(--stop-red), var(--stop-red-dark));
  }
  .chiller__action--start { background: var(--start-grey); }

  /* Bottom bars */
  .system-bar {
    left: 27px; top: 727px; width: 468px; height: 40px; z-index: 3;
    background: var(--panel); border: 1px solid var(--panel-edge); border-radius: 4px;
  }
  .system-bar__status {
    position: absolute; left: 4px; top: 4px; width: 207px; height: 30px; border-radius: 3px;
    background: var(--run-green); font-size: 11.5px; line-height: 30px; padding-left: 12px;
  }
  .system-bar__status span { position: absolute; left: 141px; font-size: 10px; }
  .system-bar__stop {
    position: absolute; left: 219px; top: 4px; width: 126px; height: 30px; border-radius: 3px;
    background: linear-gradient(var(--stop-red), var(--stop-red-dark));
    display: flex; align-items: center; justify-content: center; gap: 8px; font-size: 11px;
  }
  .system-bar__settings {
    position: absolute; left: 357px; top: 0; width: 110px; height: 38px; border-left: 1px solid var(--panel-edge);
    display: flex; align-items: center; justify-content: center; gap: 6px; font-size: 10px; font-weight: 600;
  }
  .mode-bar {
    left: 533px; top: 727px; width: 662px; height: 40px; z-index: 3;
    background: var(--panel); border: 1px solid var(--panel-edge); border-radius: 4px;
  }
  .mode-bar__label { position: absolute; left: 19px; top: 0; line-height: 38px; font-size: 10px; font-weight: 600; }
  .mode-bar__value { position: absolute; left: 100px; width: 340px; text-align: center; line-height: 38px; font-size: 22px; }
  .mode-bar__switch {
    position: absolute; right: -1px; top: -1px; width: 209px; height: 40px;
    border: 1px solid #b00; border-radius: 0 4px 4px 0;
    background: linear-gradient(90deg, #2a0000, #7a0000);
    text-align: center; line-height: 38px; font-size: 11px;
  }
</style>
</head>
<body>
<div class="stage">

  <div class="abs control-frame"></div>

  <!-- Pump cards -->
  <div class="pump-card" style="top:82px">
    <div class="pump-card__title">PUMP #1 ONLINE TIME</div>
    <div class="pump-card__time">72h 29m 42s</div>
  </div>
  <div class="pump-card" style="top:232px">
    <div class="pump-card__title">PUMP #2 ONLINE TIME</div>
    <div class="pump-card__time">72h 29m 42s</div>
  </div>
  <div class="pump-card" style="top:406px">
    <div class="pump-card__title">PUMP #3 ONLINE TIME</div>
    <div class="pump-card__time">72h 29m 42s</div>
  </div>
  <div class="pump-card" style="top:556px">
    <div class="pump-card__title">PUMP #4 ONLINE TIME</div>
    <div class="pump-card__time">72h 29m 42s</div>
  </div>

  <!-- Piping -->
  <svg class="pipes" viewBox="0 0 1253 783" aria-hidden="true">
    <g>
      <path class="pipe-c" d="M26 43 H1040 M585 43 V62 M812 43 V62 M1040 43 V62 M510 43 V385 H1040 M585 385 V404 M812 385 V404 M1040 385 V404"/>
      <path class="pipe-c-core" d="M26 43 H1040 M510 43 V385 H1040"/>
      <polygon class="arrow-c" points="6,43 30,30 30,56"/>
      <polygon class="arrow-c" points="585,55 572,74 598,74"/>
      <polygon class="arrow-c" points="812,55 799,74 825,74"/>
      <polygon class="arrow-c" points="1040,55 1027,74 1053,74"/>
      <polygon class="arrow-c" points="585,397 572,416 598,416"/>
      <polygon class="arrow-c" points="812,397 799,416 825,416"/>
      <polygon class="arrow-c" points="1040,397 1027,416 1053,416"/>
    </g>
    <g>
      <path class="pipe-y" d="M686 14 H1237 V697 H425 V667 M686 14 V58 M912 14 V58 M1138 14 V58 M686 356 H1237 M686 356 V400 M912 356 V400 M1138 356 V400"/>
      <path class="pipe-y" d="M420 222 V437 M420 222 H462 M420 437 H462"/>
      <path class="pipe-y" d="M6 327 H361 M80 327 V178 H175 M220 178 H315 V327"/>
      <path class="pipe-y" d="M6 652 H361 M80 652 V503 H175 M220 503 H315 V652"/>
      <path class="pipe-y-core" d="M686 14 H1237 V697 H425 V667 M686 356 H1237 M420 222 V437 M420 222 H462 M420 437 H462 M6 327 H361 M80 327 V178 H175 M220 178 H315 V327 M6 652 H361 M80 652 V503 H175 M220 503 H315 V652"/>
      <polygon class="arrow-y" points="686,75 673,56 699,56"/>
      <polygon class="arrow-y" points="912,75 899,56 925,56"/>
      <polygon class="arrow-y" points="1138,75 1125,56 1151,56"/>
      <polygon class="arrow-y" points="686,417 673,398 699,398"/>
      <polygon class="arrow-y" points="912,417 899,398 925,398"/>
      <polygon class="arrow-y" points="1138,417 1125,398 1151,398"/>
      <polygon class="arrow-y" points="480,222 460,209 460,235"/>
      <polygon class="arrow-y" points="480,437 460,424 460,450"/>
    </g>
  </svg>

  <!-- Pump artwork areas and reset buttons -->
  <div class="pump-overlay" style="top:82px">
    <div class="pump-overlay__art" role="img" aria-label="Illustration of pump 1 on its pipe"></div>
    <div class="pump-overlay__reset">RESET HOURS</div>
  </div>
  <div class="pump-overlay" style="top:232px">
    <div class="pump-overlay__art" role="img" aria-label="Illustration of pump 2 on its pipe"></div>
    <div class="pump-overlay__reset">RESET HOURS</div>
  </div>
  <div class="pump-overlay" style="top:406px">
    <div class="pump-overlay__art" role="img" aria-label="Illustration of pump 3 on its pipe"></div>
    <div class="pump-overlay__reset">RESET HOURS</div>
  </div>
  <div class="pump-overlay" style="top:556px">
    <div class="pump-overlay__art" role="img" aria-label="Illustration of pump 4 on its pipe"></div>
    <div class="pump-overlay__reset">RESET HOURS</div>
  </div>

  <!-- Loop readings -->
  <div class="reading reading--cyan" style="left:374px;top:29px;width:104px;height:31px">12.1°C</div>
  <div class="reading reading--yellow" style="left:361px;top:311px;width:129px;height:32px">12.1°C</div>

  <div class="abs target">
    <div class="target__title">TARGET TEMPERATURE</div>
    <div class="target__value">12°C</div>
    <div class="target__btn" style="left:5px">−</div>
    <div class="target__btn" style="left:67px">+</div>
  </div>
  <div class="reading reading--yellow" style="left:361px;top:636px;width:129px;height:31px">12.1°C</div>

  <!-- Chiller #1 -->
  <div class="chiller" style="left:533px;top:77px">
    <div class="chiller__name">CHILLER #1</div>
    <div class="chiller__temps"><div class="chiller__temp">12.1°C</div><div class="chiller__temp">12.1°C</div></div>
    <div class="label" style="left:11px;top:44px">INPUT PRESSURE</div><div class="field" style="left:10px;top:58px">13</div><div class="unit" style="left:77px;top:61px">BAR</div>
    <div class="label" style="left:118px;top:44px">INPUT PRESSURE</div><div class="field" style="left:117px;top:58px">13</div><div class="unit" style="left:184px;top:61px">BAR</div>
    <div class="label" style="left:11px;top:78px">HEAT UNIT</div><div class="field" style="left:10px;top:92px">13</div><div class="unit" style="left:77px;top:95px">HP</div>
    <div class="label" style="left:118px;top:78px">HEAT UNIT</div><div class="field" style="left:117px;top:92px">13</div><div class="unit" style="left:184px;top:95px">HP</div>
    <div class="label" style="left:11px;top:113px">ONLINE TIME</div><div class="field" style="left:10px;top:127px">13</div><div class="unit" style="left:77px;top:130px">LP</div>
    <div class="label" style="left:118px;top:113px">ONLINE TIME</div><div class="field" style="left:117px;top:127px">13</div><div class="unit" style="left:184px;top:130px">LP</div>
    <div class="label" style="left:11px;top:166px">STATUS</div><div class="pill pill--running" style="top:163px">RUNNING</div>
    <div class="label" style="left:11px;top:191px">ONLINE TIME</div><div class="pill pill--time" style="top:188px">72h 29m 42s</div>
    <div class="chiller__action">STOP</div>
  </div>

  <!-- Chiller #2 -->
  <div class="chiller" style="left:760px;top:77px">
    <div class="chiller__name">CHILLER #2</div>
    <div class="chiller__temps"><div class="chiller__temp">12.1°C</div><div class="chiller__temp">12.1°C</div></div>
    <div class="label" style="left:11px;top:44px">INPUT PRESSURE</div><div class="field" style="left:10px;top:58px">13</div><div class="unit" style="left:77px;top:61px">BAR</div>
    <div class="label" style="left:118px;top:44px">INPUT PRESSURE</div><div class="field" style="left:117px;top:58px">13</div><div class="unit" style="left:184px;top:61px">BAR</div>
    <div class="label" style="left:11px;top:78px">HEAT UNIT</div><div class="field" style="left:10px;top:92px">13</div><div class="unit" style="left:77px;top:95px">HP</div>
    <div class="label" style="left:118px;top:78px">HEAT UNIT</div><div class="field" style="left:117px;top:92px">13</div><div class="unit" style="left:184px;top:95px">HP</div>
    <div class="label" style="left:11px;top:113px">ONLINE TIME</div><div class="field" style="left:10px;top:127px">13</div><div class="unit" style="left:77px;top:130px">LP</div>
    <div class="label" style="left:118px;top:113px">ONLINE TIME</div><div class="field" style="left:117px;top:127px">13</div><div class="unit" style="left:184px;top:130px">LP</div>
    <div class="label" style="left:11px;top:166px">STATUS</div><div class="pill pill--running" style="top:163px">RUNNING</div>
    <div class="label" style="left:11px;top:191px">ONLINE TIME</div><div class="pill pill--time" style="top:188px">72h 29m 42s</div>
    <div class="chiller__action">STOP</div>
  </div>

  <!-- Chiller #3 -->
  <div class="chiller" style="left:986px;top:77px">
    <div class="chiller__name">CHILLER #3</div>
    <div class="chiller__temps"><div class="chiller__temp">12.1°C</div><div class="chiller__temp">12.1°C</div></div>
    <div class="label" style="left:11px;top:44px">INPUT PRESSURE</div><div class="field" style="left:10px;top:58px">13</div><div class="unit" style="left:77px;top:61px">BAR</div>
    <div class="label" style="left:118px;top:44px">INPUT PRESSURE</div><div class="field" style="left:117px;top:58px">13</div><div class="unit" style="left:184px;top:61px">BAR</div>
    <div class="label" style="left:11px;top:78px">HEAT UNIT</div><div class="field" style="left:10px;top:92px">13</div><div class="unit" style="left:77px;top:95px">HP</div>
    <div class="label" style="left:118px;top:78px">HEAT UNIT</div><div class="field" style="left:117px;top:92px">13</div><div class="unit" style="left:184px;top:95px">HP</div>
    <div class="label" style="left:11px;top:113px">ONLINE TIME</div><div class="field" style="left:10px;top:127px">13</div><div class="unit" style="left:77px;top:130px">LP</div>
    <div class="label" style="left:118px;top:113px">ONLINE TIME</div><div class="field" style="left:117px;top:127px">13</div><div class="unit" style="left:184px;top:130px">LP</div>
    <div class="label" style="left:11px;top:166px">STATUS</div><div class="pill pill--paused" style="top:163px">PAUSED</div>
    <div class="label" style="left:11px;top:191px">ONLINE TIME</div><div class="pill pill--time" style="top:188px">72h 29m 42s</div>
    <div class="chiller__action chiller__action--start">START</div>
  </div>

  <!-- Chiller #4 -->
  <div class="chiller" style="left:533px;top:419px">
    <div class="chiller__name">CHILLER #4</div>
    <div class="chiller__temps"><div class="chiller__temp">12.1°C</div><div class="chiller__temp">12.1°C</div></div>
    <div class="label" style="left:11px;top:44px">INPUT PRESSURE</div><div class="field" style="left:10px;top:58px">13</div><div class="unit" style="left:77px;top:61px">BAR</div>
    <div class="label" style="left:118px;top:44px">INPUT PRESSURE</div><div class="field" style="left:117px;top:58px">13</div><div class="unit" style="left:184px;top:61px">BAR</div>
    <div class="label" style="left:11px;top:78px">HEAT UNIT</div><div class="field" style="left:10px;top:92px">13</div><div class="unit" style="left:77px;top:95px">HP</div>
    <div class="label" style="left:118px;top:78px">HEAT UNIT</div><div class="field" style="left:117px;top:92px">13</div><div class="unit" style="left:184px;top:95px">HP</div>
    <div class="label" style="left:11px;top:113px">ONLINE TIME</div><div class="field" style="left:10px;top:127px">13</div><div class="unit" style="left:77px;top:130px">LP</div>
    <div class="label" style="left:118px;top:113px">ONLINE TIME</div><div class="field" style="left:117px;top:127px">13</div><div class="unit" style="left:184px;top:130px">LP</div>
    <div class="label" style="left:11px;top:166px">STATUS</div><div class="pill pill--running" style="top:163px">RUNNING</div>
    <div class="label" style="left:11px;top:191px">ONLINE TIME</div><div class="pill pill--time" style="top:188px">72h 29m 42s</div>
    <div class="chiller__action">STOP</div>
  </div>

  <!-- Chiller #5 -->
  <div class="chiller" style="left:760px;top:419px">
    <div class="chiller__name">CHILLER #5</div>
    <div class="chiller__temps"><div class="chiller__temp">12.1°C</div><div class="chiller__temp">12.1°C</div></div>
    <div class="label" style="left:11px;top:44px">INPUT PRESSURE</div><div class="field" style="left:10px;top:58px">13</div><div class="unit" style="left:77px;top:61px">BAR</div>
    <div class="label" style="left:118px;top:44px">INPUT PRESSURE</div><div class="field" style="left:117px;top:58px">13</div><div class="unit" style="left:184px;top:61px">BAR</div>
    <div class="label" style="left:11px;top:78px">HEAT UNIT</div><div class="field" style="left:10px;top:92px">13</div><div class="unit" style="left:77px;top:95px">HP</div>
    <div class="label" style="left:118px;top:78px">HEAT UNIT</div><div class="field" style="left:117px;top:92px">13</div><div class="unit" style="left:184px;top:95px">HP</div>
    <div class="label" style="left:11px;top:113px">ONLINE TIME</div><div class="field" style="left:10px;top:127px">13</div><div class="unit" style="left:77px;top:130px">LP</div>
    <div class="label" style="left:118px;top:113px">ONLINE TIME</div><div class="field" style="left:117px;top:127px">13</div><div class="unit" style="left:184px;top:130px">LP</div>
    <div class="label" style="left:11px;top:166px">STATUS</div><div class="pill pill--running" style="top:163px">RUNNING</div>
    <div class="label" style="left:11px;top:191px">ONLINE TIME</div><div class="pill pill--time" style="top:188px">72h 29m 42s</div>
    <div class="chiller__action">STOP</div>
  </div>

  <!-- Chiller #6 -->
  <div class="chiller" style="left:986px;top:419px">
    <div class="chiller__name">CHILLER #6</div>
    <div class="chiller__temps"><div class="chiller__temp">12.1°C</div><div class="chiller__temp">12.1°C</div></div>
    <div class="label" style="left:11px;top:44px">INPUT PRESSURE</div><div class="field" style="left:10px;top:58px">13</div><div class="unit" style="left:77px;top:61px">BAR</div>
    <div class="label" style="left:118px;top:44px">INPUT PRESSURE</div><div class="field" style="left:117px;top:58px">13</div><div class="unit" style="left:184px;top:61px">BAR</div>
    <div class="label" style="left:11px;top:78px">HEAT UNIT</div><div class="field" style="left:10px;top:92px">13</div><div class="unit" style="left:77px;top:95px">HP</div>
    <div class="label" style="left:118px;top:78px">HEAT UNIT</div><div class="field" style="left:117px;top:92px">13</div><div class="unit" style="left:184px;top:95px">HP</div>
    <div class="label" style="left:11px;top:113px">ONLINE TIME</div><div class="field" style="left:10px;top:127px">13</div><div class="unit" style="left:77px;top:130px">LP</div>
    <div class="label" style="left:118px;top:113px">ONLINE TIME</div><div class="field" style="left:117px;top:127px">13</div><div class="unit" style="left:184px;top:130px">LP</div>
    <div class="label" style="left:11px;top:166px">STATUS</div><div class="pill pill--running" style="top:163px">RUNNING</div>
    <div class="label" style="left:11px;top:191px">ONLINE TIME</div><div class="pill pill--time" style="top:188px">72h 29m 42s</div>
    <div class="chiller__action">STOP</div>
  </div>

  <!-- System controls -->
  <div class="abs system-bar">
    <div class="system-bar__status">SYSTEM STATUS:<span>RUNNING</span></div>
    <div class="system-bar__stop">
      <svg width="18" height="18" viewBox="0 0 18 18" aria-hidden="true"><path d="M5.2 4.2 A6.5 6.5 0 1 0 12.8 4.2" fill="none" stroke="#fff" stroke-width="2" stroke-linecap="round"/><line x1="9" y1="1.5" x2="9" y2="8.5" stroke="#fff" stroke-width="2" stroke-linecap="round"/></svg>
      STOP
    </div>
    <div class="system-bar__settings">
      <svg width="12" height="12" viewBox="0 0 12 12" aria-hidden="true"><circle cx="6" cy="6" r="3.6" fill="none" stroke="#fff" stroke-width="2.2" stroke-dasharray="2 1.2"/><circle cx="6" cy="6" r="1.4" fill="#fff"/></svg>
      SETTINGS
    </div>
  </div>

  <div class="abs mode-bar">
    <div class="mode-bar__label">MODE :</div>
    <div class="mode-bar__value">COOLING MODE</div>
    <div class="mode-bar__switch">CHANGE TO HEATING MODE</div>
  </div>

</div>
</body>
</html>
```